I have an animal hospital. I want a poster to hang in each exam room to show a picture of a normal sized heart and then an enlarged heart of a dog that was fed a grain-free diet. I want to warn people not to feed grain-free diets. Maybe at the top of the poster, "Do you feed grain-free?" and then the x-ray comparison, then the warnings of Canine Dilated Cardiomyopathy.

```html
<!DOCTYPE html>
<html lang="en">
<head>
<meta charset="utf-8">
<title>Do You Feed Grain-Free? – DCM Awareness Poster</title>
<link href="https://fonts.googleapis.com/css2?family=Montserrat:wght@400;500;700;800&family=Playfair+Display:wght@900&display=swap" rel="stylesheet">
<style>
  :root {
    --orange: #ec6d33;
    --charcoal: #5f5b5c;
    --mist: #efefef;
    --amber: #f7b316;
    --ink: #2b2b2b;
    --white: #ffffff;
  }
  * { margin: 0; padding: 0; box-sizing: border-box; }
  html, body { width: 849px; height: 1200px; overflow: hidden; background: var(--white); }
  .poster {
    position: relative; width: 849px; height: 1200px; overflow: hidden;
    background: var(--white); font-family: "Montserrat", Arial, sans-serif; color: var(--ink);
  }
  .backdrop { position: absolute; inset: 0; width: 849px; height: 1200px; }

  .headline { position: absolute; left: 22px; top: 42px; z-index: 2; }
  .headline span { display: block; font-weight: 800; line-height: 1; }
  .headline .do-you { color: var(--charcoal); font-size: 62px; letter-spacing: -1px; }
  .headline .feed { color: var(--orange); font-size: 128px; letter-spacing: -4px; margin-top: -18px; margin-left: 4px; }
  .headline .grain-free { color: var(--charcoal); font-size: 51px; letter-spacing: -1px; margin-top: -16px; }
  .question-mark {
    position: absolute; left: 372px; top: -8px;
    font-family: "Playfair Display", Georgia, serif; font-weight: 900;
    font-size: 330px; line-height: 1; color: var(--charcoal);
  }

  .xray-card { position: absolute; background: var(--charcoal); padding: 12px; }
  .xray-card.normal { left: 62px; top: 288px; width: 342px; height: 480px; transform: rotate(-2deg); }
  .xray-card.enlarged { left: 412px; top: 278px; width: 390px; height: 540px; transform: rotate(2deg); }
  .xray-image {
    width: 100%; height: 100%;
    background: radial-gradient(ellipse 40% 35% at 50% 58%, #d9d9d9 0%, #9a9a9a 55%, transparent 80%),
                linear-gradient(90deg, #1a1a1a 0%, #8a8a8a 22%, #b5b5b5 50%, #8a8a8a 78%, #1a1a1a 100%);
  }
  .xray-card.enlarged .xray-image {
    background: radial-gradient(ellipse 45% 30% at 50% 62%, #e4e4e4 0%, #a8a8a8 60%, transparent 85%),
                linear-gradient(90deg, #050505 0%, #050505 14%, #9a9a9a 30%, #c0c0c0 50%, #9a9a9a 70%, #050505 86%, #050505 100%);
  }
  .xray-label {
    position: absolute; background: var(--orange); color: var(--white);
    font-weight: 700; text-transform: uppercase; white-space: nowrap;
  }
  .normal .xray-label { right: 16px; top: 10px; font-size: 20px; padding: 12px 12px 10px 16px; letter-spacing: 0.5px; }
  .enlarged .xray-label { left: 8px; top: 0; font-size: 27px; padding: 10px 14px 14px 14px; letter-spacing: 0.5px; }
  .warning-icon { position: absolute; left: 398px; top: 632px; width: 150px; height: 160px; }

  .intro { position: absolute; left: 24px; top: 795px; font-size: 12.6px; font-weight: 500; }
  .check-list { list-style: none; position: absolute; }
  .check-list li {
    position: relative; color: var(--orange); font-weight: 700; font-size: 15px; line-height: 1.2;
    padding-left: 27px; white-space: nowrap;
  }
  .check-list li svg { position: absolute; left: 0; top: 2px; width: 19px; height: 17px; }
  .symptoms-a { left: 24px; top: 822px; }
  .symptoms-b { left: 235px; top: 822px; }
  .symptoms-a li, .symptoms-b li { height: 26px; }
  .symptoms-b li { padding-left: 23px; }

  .note { position: absolute; left: 22px; font-size: 12.4px; font-weight: 500; line-height: 15px; white-space: nowrap; }
  .note.preclinical { top: 933px; }
  .note.exam { top: 975px; }

  .signs { left: 22px; top: 1018px; }
  .signs li { font-size: 14.4px; padding-left: 33px; margin-bottom: 8.5px; line-height: 17.5px; }
  .signs li:last-child { line-height: 26px; margin-top: -4px; }
  .signs li svg { top: 1px; width: 21px; height: 19px; }

  .dog-photo {
    position: absolute; left: 602px; top: 860px; width: 247px; height: 340px;
    border-radius: 120px 100px 0 40px;
    background: radial-gradient(ellipse 60% 40% at 45% 30%, #c46a3a 0%, #a4552b 55%, #7d3f1f 100%);
  }
</style>
</head>
<body>
<main class="poster">
  <svg class="backdrop" viewBox="0 0 849 1200" aria-hidden="true">
    <path d="M0 0 H270 C275 40 250 60 210 55 C150 50 130 120 110 170 C95 210 60 235 0 215 Z" fill="var(--mist)"/>
    <path d="M680 0 H849 V365 C820 350 790 320 780 280 C770 240 800 210 815 180 C830 140 800 110 760 95 C720 80 690 40 680 0 Z" fill="var(--orange)"/>
    <path d="M705 90 C720 130 760 140 790 160 C810 175 815 190 810 205" fill="none" stroke="var(--white)" stroke-width="1.6"/>
    <path d="M712 95 C730 135 770 145 798 165 C815 178 818 192 813 210" fill="none" stroke="var(--white)" stroke-width="1.6"/>
    <path d="M0 1090 C60 1075 120 1090 140 1120 C155 1150 180 1170 230 1175 C260 1180 275 1195 275 1200 H0 Z" fill="var(--mist)"/>
    <path d="M620 990 C630 960 680 940 720 935 C780 925 820 930 849 940 V1200 H528 C528 1165 560 1135 600 1130 C630 1125 640 1080 630 1050 C622 1030 612 1010 620 990 Z" fill="var(--orange)"/>
  </svg>

  <h1 class="headline">
    <span class="do-you">DO YOU</span>
    <span class="feed">FEED</span>
    <span class="grain-free">GRAIN-FREE?</span>
  </h1>
  <div class="question-mark" aria-hidden="true">?</div>

  <figure class="xray-card normal">
    <div class="xray-image" role="img" aria-label="Chest x-ray of a dog with a normal sized heart"></div>
    <figcaption class="xray-label">Normal Heart</figcaption>
  </figure>
  <figure class="xray-card enlarged">
    <div class="xray-image" role="img" aria-label="Chest x-ray of a dog with an enlarged heart"></div>
    <figcaption class="xray-label">Enlarged Heart</figcaption>
  </figure>
  <svg class="warning-icon" viewBox="0 0 150 160" aria-hidden="true">
    <path d="M50 10 L140 110 Q145 120 135 124 L15 150 Q3 152 4 140 L40 16 Q44 6 50 10 Z" fill="none" stroke="var(--amber)" stroke-width="7" stroke-linejoin="round"/>
    <path d="M52 42 L66 40 L68 100 L60 102 Z" fill="var(--amber)"/>
    <rect x="60" y="110" width="13" height="13" fill="var(--amber)" transform="rotate(-8 66 116)"/>
  </svg>

  <p class="intro">The major symptoms of DCM include:</p>

  <svg width="0" height="0" style="position:absolute">
    <defs>
      <symbol id="tick" viewBox="0 0 20 18"><path d="M1 9.5 L4.5 7 L8 11 L17 1 L19.5 3 L8 16.5 Z" fill="var(--orange)"/></symbol>
    </defs>
  </svg>

  <ul class="check-list symptoms-a">
    <li><svg><use href="#tick"/></svg>Lethargy</li>
    <li><svg><use href="#tick"/></svg>Anorexia</li>
    <li><svg><use href="#tick"/></svg>Labored breathing</li>
    <li><svg><use href="#tick"/></svg>Panting</li>
  </ul>
  <ul class="check-list symptoms-b">
    <li><svg><use href="#tick"/></svg>Coughing</li>
    <li><svg><use href="#tick"/></svg>Abdominal distension</li>
    <li><svg><use href="#tick"/></svg>Sudden collapse</li>
  </ul>

  <p class="note preclinical">In some cases, dogs with preclinical DCM (prior to the appearance of symptoms)<br>may be given a questionable diagnosis if they appear to be in fine health.</p>
  <p class="note exam">On the other hand, a thorough physical exam can reveal some<br>of the subtle symptoms of DCM, such as:</p>

  <div class="dog-photo" role="img" aria-label="Photo of a russet-coated dog looking up with a tilted head"></div>

  <ul class="check-list signs">
    <li><svg><use href="#tick"/></svg>Pulse deficits</li>
    <li><svg><use href="#tick"/></svg>Premature heart contractions that originate in or above the ventricles</li>
    <li><svg><use href="#tick"/></svg>Slow capillary refill time in the mucous membrane tissues<br>(e.g., gums are slow to turn pink again after pressing on them<br>gently), indicating poor circulation</li>
    <li><svg><use href="#tick"/></svg>Breathing sounds muffled or crackly due to the presence<br>of fluid in the lungs</li>
  </ul>
</main>
</body>
</html>
```